RPN FORMED

building services
decks
pergola
renovation
extensions
general building

Target Market(s)

middle to upper class

Industry/Entity Type

building

Contact Information for Business Card

my details 0438917264 tkbarrow47@mailvora.com BLD581047

Font styles to use
Serif

Colors
00AB8E
00BBA5
67D7C9
C6EFE9
E9F9F6

Requirements
Must have
• logo on the front and details on the back
Nice to have
• sharp and clean lines

```html
<!DOCTYPE html>
<html lang="en">
<head>
<meta charset="utf-8">
<title>RPN FORMED – Business Card</title>
<link rel="stylesheet" href="https://fonts.googleapis.com/css2?family=EB+Garamond:wght@500;700&family=Fira+Sans:wght@400&display=swap">
<style>
  :root {
    --backdrop: #9a9a9a;
    --card: #ffffff;
    --green: #05b870;
    --ink: #111111;
    --band: #1e1e1e;
    --on-green: #ffffff;
  }
  * { margin: 0; padding: 0; box-sizing: border-box; }
  html, body {
    width: 1133px; height: 1200px; overflow: hidden;
    background: var(--backdrop);
  }
  .card {
    position: absolute;
    background: var(--card);
    overflow: hidden;
  }
  .card-front { left: 192px; top: 139px; width: 734px; height: 417px; }
  .card-back  { left: 196px; top: 641px; width: 728px; height: 416px; }
  .wave { position: absolute; inset: 0; width: 100%; height: 100%; }
  .wordmark {
    position: absolute;
    font-family: "EB Garamond", serif;
    font-weight: 700;
    font-size: 50px;
    line-height: 1;
    color: var(--ink);
    letter-spacing: -0.3px;
    white-space: nowrap;
  }
  .card-front .wordmark { right: 96px; top: 98px; }
  .card-back .wordmark { left: 67px; top: 100px; }
  .contact {
    position: absolute; left: 32px; top: 262px;
    font-family: "EB Garamond", serif;
    color: var(--on-green);
  }
  .contact-name { font-weight: 700; font-size: 28px; line-height: 1; letter-spacing: 0.3px; }
  .contact-role { font-weight: 500; font-size: 17px; line-height: 1; margin-top: 4px; }
  .contact-line {
    display: flex; align-items: center; gap: 10px;
    font-weight: 500; font-size: 17px; line-height: 1;
    margin-top: 8px;
  }
  .contact-line:first-of-type { margin-top: 14px; }
  .contact-line svg { width: 14px; height: 14px; flex: none; }
  .licence { font-weight: 500; font-size: 17px; line-height: 1; margin-top: 14px; }
  .services {
    position: absolute; right: 48px; top: 253px;
    list-style: none;
    font-family: "Fira Sans", sans-serif;
    font-size: 17px; line-height: 22.4px;
    color: var(--on-green);
    text-align: right;
  }
  .services li { display: flex; justify-content: flex-end; align-items: center; gap: 13px; }
  .services svg { width: 14px; height: 14px; flex: none; }
</style>
</head>
<body>

<section class="card card-front" aria-label="Business card front">
  <svg class="wave" viewBox="0 0 851 484" preserveAspectRatio="none" aria-hidden="true">
    <path fill="var(--green)" d="M0,251 C40,218 85,205 128,205 C260,205 420,320 560,392 C640,432 690,462 728,484 L0,484 Z"/>
    <path fill="var(--band)" d="M110,204 C190,192 300,232 430,300 C570,372 700,456 851,452 L851,477 C700,480 560,418 440,345 C325,276 225,213 110,204 Z"/>
  </svg>
  <div class="wordmark">RPN FORMED</div>
  <div class="contact">
    <div class="contact-name">DANIEL HARPER</div>
    <div class="contact-role">President</div>
    <div class="contact-line">
      <svg viewBox="0 0 16 16" aria-hidden="true"><path fill="currentColor" d="M3.6 1.2 6 3.6 4.8 5.6c.8 2 2.6 3.8 4.6 4.6l2-1.2 2.4 2.4-1.6 2.4C7 13.6 2.4 9 1.2 2.8Z"/></svg>
      <span>0438917264</span>
    </div>
    <div class="contact-line">
      <svg viewBox="0 0 16 16" aria-hidden="true"><rect x="1" y="3.5" width="14" height="9" fill="currentColor"/><path d="M1.5 4 8 9l6.5-5" fill="none" stroke="var(--green)" stroke-width="1.3"/></svg>
      <span>tkbarrow47@mailvora.com</span>
    </div>
    <div class="licence">BLD581047</div>
  </div>
</section>

<section class="card card-back" aria-label="Business card back">
  <svg class="wave" viewBox="0 0 851 484" preserveAspectRatio="none" aria-hidden="true">
    <g transform="translate(851 0) scale(-1 1)">
      <path fill="var(--green)" d="M0,251 C40,218 85,205 128,205 C260,205 420,320 560,392 C640,432 690,462 728,484 L0,484 Z"/>
      <path fill="var(--band)" d="M110,204 C190,192 300,232 430,300 C570,372 700,456 851,452 L851,477 C700,480 560,418 440,345 C325,276 225,213 110,204 Z"/>
    </g>
  </svg>
  <div class="wordmark">RPN FORMED</div>
  <ul class="services">
    <li>Building Services <svg viewBox="0 0 16 16" aria-hidden="true"><rect x="1.5" y="3" width="11.5" height="11.5" fill="none" stroke="currentColor" stroke-width="2"/><path d="M4.5 8.5 7 11l7-8.5" fill="none" stroke="currentColor" stroke-width="2"/></svg></li>
    <li>Decks <svg viewBox="0 0 16 16" aria-hidden="true"><rect x="1.5" y="3" width="11.5" height="11.5" fill="none" stroke="currentColor" stroke-width="2"/><path d="M4.5 8.5 7 11l7-8.5" fill="none" stroke="currentColor" stroke-width="2"/></svg></li>
    <li>Pergola <svg viewBox="0 0 16 16" aria-hidden="true"><rect x="1.5" y="3" width="11.5" height="11.5" fill="none" stroke="currentColor" stroke-width="2"/><path d="M4.5 8.5 7 11l7-8.5" fill="none" stroke="currentColor" stroke-width="2"/></svg></li>
    <li>Renovation <svg viewBox="0 0 16 16" aria-hidden="true"><rect x="1.5" y="3" width="11.5" height="11.5" fill="none" stroke="currentColor" stroke-width="2"/><path d="M4.5 8.5 7 11l7-8.5" fill="none" stroke="currentColor" stroke-width="2"/></svg></li>
    <li>Extensions <svg viewBox="0 0 16 16" aria-hidden="true"><rect x="1.5" y="3" width="11.5" height="11.5" fill="none" stroke="currentColor" stroke-width="2"/><path d="M4.5 8.5 7 11l7-8.5" fill="none" stroke="currentColor" stroke-width="2"/></svg></li>
    <li>General Building <svg viewBox="0 0 16 16" aria-hidden="true"><rect x="1.5" y="3" width="11.5" height="11.5" fill="none" stroke="currentColor" stroke-width="2"/><path d="M4.5 8.5 7 11l7-8.5" fill="none" stroke="currentColor" stroke-width="2"/></svg></li>
  </ul>
</section>

</body>
</html>
```